Professional & Modern Technology Business Card

We need a business card for our software/technology firm. Our services include Program/Project Management, Project Controls and Enterprise Analytics. Our clients are usually in the Aviation, Public Works, Transportation and Electric & Water Utility industries. We serve both public and private clients. Would like a very professional, conservative but somewhat modern design. Design, Develop, Deploy is the corporate tagline. We have two offices. The headquarters is in Atlanta, GA and a satellite office In Savannah, GA. Corporate Logo Attached.
Looking to do website and corporate brochure after the successful completion of this project. Would like to begin a working relationship with best designers.
Tagline: Design, Develop, Deploy
Website: www.quelvanesystems.example
My Name: Marla Dunstead
My Title: CEO
Email: mdunstead@quelvanesystems.example
Atlanta Address:
87 Corliss Avenue, #2291
Atlanta, GA 30301
Office: 404.555.0182
Fax: 404.555.0147
Mobile: 404.555.0163
Savannah Address:
350 West Harrow Bend Road
Suite 720
Savannah, GA 31401
Office: 912.555.0139
Fax: 404.555.0147
Mobile: 404.555.0163
Updates
Please include the email address in your designs: mdunstead@quelvanesystems.example.
I appreciate everyone's design efforts. Just a few notes:
1. Please remove the mobile number from the cards
2. The backs of the cards can be utilized for writing notes. Make sure your design on the back of the card is conducive to clearly adding writing if needed.
3. No black backgrounds please
4. Only use the corporate logo on the front of the card. You can use portions of the logo design, but not the logo in totality.
Thank You
Industry/Entity Type
Conservative
Look and feel
Each slider illustrates characteristics of the customer's brand and the style your logo design should communicate.

```html
<!DOCTYPE html>
<html lang="en">
<head>
<meta charset="utf-8">
<title>Quelvane Systems, Inc. — Business Card</title>
<link rel="stylesheet" href="https://fonts.googleapis.com/css2?family=Arimo:wght@400;700&display=swap">
<style>
  :root {
    --stage: #e9eaec;
    --card: #ffffff;
    --ink: #2b2626;
    --ink-soft: #3c3838;
    --muted: #6b6666;
    --icon-blue: #1a8fd6;
    --accent: #e6c800;
    --faint: #f1f1f1;
    --shadow: rgba(0,0,0,0.18);
  }
  * { box-sizing: border-box; margin: 0; padding: 0; }
  html, body { width: 1200px; height: 848px; overflow: hidden; }
  body {
    background: var(--stage);
    font-family: "Arimo", Arial, sans-serif;
    color: var(--ink);
    position: relative;
  }
  .card {
    position: absolute;
    width: 520px;
    height: 298px;
    background: var(--card);
    border-radius: 16px;
    box-shadow: 0 6px 20px var(--shadow);
    overflow: hidden;
  }
  .card--info { left: 50px; top: 275px; }
  .card--brand {
    left: 630px; top: 275px;
    display: flex; flex-direction: column; align-items: center; justify-content: center;
    gap: 14px;
  }

  .wordmark {
    display: flex;
    align-items: center;
    gap: 10px;
    font-weight: 700;
    color: var(--ink);
    white-space: nowrap;
  }
  .wordmark__dot { border-radius: 50%; background: var(--accent); flex: none; }
  .card--info .wordmark { position: absolute; left: 40px; top: 112px; font-size: 22px; }
  .card--info .wordmark__dot { width: 22px; height: 22px; }
  .card--brand .wordmark { font-size: 34px; }
  .card--brand .wordmark__dot { width: 34px; height: 34px; }

  .tagline {
    font-size: 13px;
    letter-spacing: 2.5px;
    text-transform: uppercase;
    color: var(--muted);
  }

  .holder { position: absolute; right: 30px; top: 28px; text-align: right; }
  .holder__name { font-size: 17px; font-weight: 700; letter-spacing: 0.3px; }
  .holder__title { font-size: 12px; margin-top: 2px; }

  .faint-mark {
    position: absolute;
    right: 40px; top: 90px;
    width: 150px; height: 150px;
    border-radius: 50%;
    background: var(--faint);
  }

  .office { position: absolute; font-size: 11.5px; line-height: 15px; color: var(--ink-soft); }
  .office--atlanta { left: 40px; bottom: 30px; }
  .office--savannah { right: 30px; bottom: 30px; text-align: right; }
  .office__addr { margin-bottom: 6px; }
  .contact { display: flex; align-items: center; gap: 6px; }
  .office--savannah .contact { justify-content: flex-end; }
  .contact svg { width: 10px; height: 10px; fill: var(--icon-blue); flex: none; }
</style>
</head>
<body>
<svg width="0" height="0" style="position:absolute" aria-hidden="true">
  <defs>
    <symbol id="i-phone" viewBox="0 0 10 10"><path d="M2 0.5 L3.6 2.6 L2.8 3.6 Q4 6 6.4 7.2 L7.4 6.4 L9.5 8 L8.4 9.5 Q3.5 9 0.5 1.6 Z"/></symbol>
    <symbol id="i-fax" viewBox="0 0 10 10"><rect x="2.5" y="0.5" width="5" height="3"/><rect x="0.5" y="3.5" width="9" height="4" rx="1"/><rect x="2.5" y="6.5" width="5" height="3"/></symbol>
    <symbol id="i-mail" viewBox="0 0 10 10"><path d="M0.5 2 H9.5 V8.5 H0.5 Z"/><path d="M0.5 2 L5 5.5 L9.5 2" fill="#fff" stroke="#fff" stroke-width="0.6"/></symbol>
    <symbol id="i-globe" viewBox="0 0 10 10"><path d="M5 0.5 A4.5 4.5 0 1 0 5 9.5 A4.5 4.5 0 1 0 5 0.5 Z M5 1.5 A3.5 3.5 0 1 1 5 8.5 A3.5 3.5 0 1 1 5 1.5 Z"/><rect x="1" y="4.6" width="8" height="0.8"/><rect x="4.6" y="1" width="0.8" height="8"/></symbol>
  </defs>
</svg>

<section class="card card--info" aria-label="Business card, contact side">
  <div class="faint-mark" role="img" aria-label="Faint brand decoration area"></div>

  <div class="holder">
    <p class="holder__name">Marla Dunstead</p>
    <p class="holder__title">CEO</p>
  </div>

  <div class="wordmark"><span class="wordmark__dot"></span>Quelvane Systems, Inc.</div>

  <div class="office office--atlanta">
    <p class="office__addr">Atlanta :<br>87 Corliss Avenue, #2291<br>Atlanta, GA 30301</p>
    <p class="contact"><svg><use href="#i-phone"/></svg>404.555.0182</p>
    <p class="contact"><svg><use href="#i-fax"/></svg>404.555.0147</p>
    <p class="contact"><svg><use href="#i-mail"/></svg>mdunstead@quelvanesystems.example</p>
  </div>

  <div class="office office--savannah">
    <p class="office__addr">Savannah:<br>350 West Harrow Bend Road<br>Suite 720, Savannah, GA 31401</p>
    <p class="contact">912.555.0139<svg><use href="#i-phone"/></svg></p>
    <p class="contact">404.555.0147<svg><use href="#i-fax"/></svg></p>
    <p class="contact">www.quelvanesystems.example<svg><use href="#i-globe"/></svg></p>
  </div>
</section>

<section class="card card--brand" aria-label="Business card, brand side">
  <div class="wordmark"><span class="wordmark__dot"></span>Quelvane Systems, Inc.</div>
  <p class="tagline">Design, Develop, Deploy</p>
</section>
</body>
</html>
```